Business Card Design for Vintage Jazz

I am a vintage jazz band leader in New York City. My groups play the music of the 1920s, 1930s and 1940s. My website is marlowpeskin.com for more info on what I do.

I am looking for a two sided business card design that has the look and feel of a really nice business card from the 1930s. I need to convey with the design that my work has that vintage kind of class and style, but also conveys that we are fun and entertaining.

Most importantly it should make a bold staement. If Hollis Varnum had a card, what would it have looked like? I want a card that I feel confident will make an impact and will let people know that my work is te the top that NYC has to offer in vintage jazz..

Note that I have only decided to avoid the "committed payment" option as I have not used this service before. Assuming that I get quality work I will select a design from those presented.

Target Market(s)

people who want to hire my band for events, media, and new fans of the band

Industry/Entity Type

Performing Art

Contact Information for Business Card

Definitely a matte finish, possibly a sort of old style of paper with that brown tint? definitely a thick card.

Requirements
Must have
• FRONT
• My name: Marlow Peskin
• What I do: Bandleader, Guitarist, Vocalist, Songwriter
• Contact Details: marlowpeskin.com marlow@marlowpeskin.com 646-555-0187
• BACK
• My Social Media Links:
• facebook.marlowpeskin.com
• twitter, instagram, linkedin: marlowpeskin
• I'm also including a photo image I would like to use. The photo's background is not needed, and to be honest isn't really desireable. Just looking to use the image of me.
Nice to have
• I'm attaching which could be used as is, omitted from the card, or altered maybe with text going around the outside of the circle or in some other way. It may need some clean up to the edges of the lettering as we only use it for the website thumbnail.
• If there's space I'd like to include the text "join our mailing list for a free song download: freesong.marlowpeskin.com" If not perhaps just "Download a Free Song at: freesong.marlowpeskin.com - something to this end.
Should not have
• anything cartoony. Don't think retro 90s's vision of the swing era, think actual swing era!
• anything modern. Got to look old school
• Try to avoid dark backgrounds. Since we often play in bars and clubs where it is dar, a d
• avoid script fonts.

```html
<!DOCTYPE html>
<html lang="en">
<head>
<meta charset="utf-8">
<title>Marlow Peskin – Business Card</title>
<link href="https://fonts.googleapis.com/css2?family=Josefin+Sans:wght@400;600;700&display=swap" rel="stylesheet">
<style>
  :root {
    --backdrop: #e4e0da;
    --paper: #eadcc0;
    --paper-deep: #dcc8a3;
    --ink: #2b1d12;
    --ink-soft: #4a3726;
    --rule: #8a6a45;
    --mark-bg: #2b1d12;
    --mark-ink: #eadcc0;
    --photo-light: #c9b493;
    --photo-dark: #6f5639;
  }
  * { box-sizing: border-box; margin: 0; padding: 0; }
  html, body {
    width: 1200px; height: 814px; overflow: hidden;
    background: var(--backdrop);
    font-family: "Josefin Sans", "Century Gothic", sans-serif;
  }
  .stage { position: relative; width: 1200px; height: 814px; }

  .card {
    position: absolute; top: 252px;
    width: 540px; height: 310px;
    background: radial-gradient(ellipse at 50% 45%, var(--paper) 55%, var(--paper-deep) 100%);
    color: var(--ink);
    overflow: hidden;
    box-shadow: 0 2px 6px rgba(60, 40, 20, 0.25);
  }
  .card--front { left: 40px; }
  .card--back { left: 620px; }

  .frame {
    position: absolute; inset: 12px;
    border: 2px solid var(--rule);
    pointer-events: none;
  }
  .frame::after {
    content: ""; position: absolute; inset: 4px;
    border: 1px solid var(--rule);
  }

  .mark {
    position: absolute;
    border-radius: 50%;
    background: var(--mark-bg);
    color: var(--mark-ink);
    display: flex; align-items: center; justify-content: center;
    text-align: center;
    font-weight: 600;
    line-height: 1.2;
    letter-spacing: 1px;
    text-transform: uppercase;
  }
  .card--front .mark { left: 52px; top: 84px; width: 142px; height: 142px; font-size: 17px; }
  .card--back .mark { left: 40px; top: 34px; width: 104px; height: 104px; font-size: 13px; }

  .divider {
    position: absolute; left: 232px; top: 70px;
    width: 1px; height: 170px;
    background: var(--rule);
  }
  .identity { position: absolute; left: 256px; top: 86px; }
  .identity__name {
    font-size: 21px; font-weight: 700;
    letter-spacing: 2px; text-transform: uppercase;
  }
  .identity__role { margin-top: 4px; font-size: 15px; color: var(--ink-soft); line-height: 1.35; }

  .contact-list { list-style: none; margin-top: 12px; }
  .contact-list li {
    display: flex; align-items: center; gap: 9px;
    font-size: 15px; color: var(--ink-soft); line-height: 1.6;
  }
  .contact-list svg { width: 14px; height: 14px; flex: none; }

  .social-list { position: absolute; left: 42px; top: 150px; list-style: none; }
  .social-list li {
    display: flex; align-items: center; gap: 9px;
    font-size: 14px; color: var(--ink-soft); line-height: 1.6;
  }
  .social-list .dot {
    width: 12px; height: 12px; border-radius: 50%;
    background: var(--ink); flex: none;
  }
  .free-song {
    position: absolute; left: 42px; top: 248px;
    font-size: 13px; color: var(--ink-soft); line-height: 1.4;
  }
  .free-song strong { color: var(--ink); font-weight: 700; }

  .portrait {
    position: absolute; right: 26px; top: 20px;
    width: 216px; height: 230px;
    background: radial-gradient(ellipse at 50% 45%, var(--photo-light), var(--photo-dark) 70%, var(--paper-deep) 100%);
  }
</style>
</head>
<body>
<main class="stage">
  <section class="card card--front" aria-label="Card front">
    <div class="frame"></div>
    <div class="mark">Marlow<br>Peskin</div>
    <div class="divider"></div>
    <div class="identity">
      <p class="identity__name">Marlow Peskin</p>
      <p class="identity__role">Bandleader, Guitarist<br>Vocalist, Songwriter</p>
      <ul class="contact-list">
        <li>
          <svg viewBox="0 0 14 14" aria-hidden="true"><rect x="3" y="0.5" width="8" height="13" rx="1.5" fill="none" stroke="#2b1d12" stroke-width="1.3"/><circle cx="7" cy="11" r="0.9" fill="#2b1d12"/></svg>
          646-555-0187
        </li>
        <li>
          <svg viewBox="0 0 14 14" aria-hidden="true"><rect x="0.5" y="2.5" width="13" height="9" fill="#2b1d12"/><path d="M0.5 2.5 L7 8 L13.5 2.5" fill="none" stroke="#eadcc0" stroke-width="1.2"/></svg>
          marlow@marlowpeskin.com
        </li>
        <li>
          <svg viewBox="0 0 14 14" aria-hidden="true"><circle cx="7" cy="7" r="6.3" fill="#2b1d12"/><path d="M1 7 H13 M7 1 C3.5 4 3.5 10 7 13 M7 1 C10.5 4 10.5 10 7 13" fill="none" stroke="#eadcc0" stroke-width="1"/></svg>
          marlowpeskin.com
        </li>
      </ul>
    </div>
  </section>

  <section class="card card--back" aria-label="Card back">
    <div class="frame"></div>
    <div class="mark">Marlow<br>Peskin</div>
    <ul class="social-list">
      <li><span class="dot"></span>marlowpeskin.com</li>
      <li><span class="dot"></span>marlowpeskin</li>
      <li><span class="dot"></span>marlowpeskin</li>
      <li><span class="dot"></span>marlowpeskin</li>
    </ul>
    <p class="free-song">Download a Free Song at:<br><strong>freesong.marlowpeskin.com</strong></p>
    <div class="portrait" role="img" aria-label="Sepia photo of the bandleader in a striped-lapel jacket tipping a straw boater hat"></div>
  </section>
</main>
</body>
</html>
```